Tulvex, a future commerce website

Tulvex will be a commerce website; the project is quite large, and for now I just require three pages and the main bar to be crafted; If chosen your design, I will require you to work with me in a freelance job for the rest of the site to be made.
The following is one way to put Tulvex’s building blocks; you can propose another.
A list of webpages, whose design I like, is in the first document.
-Design specification
Tulvex’s interface should be minimal and intuitive.
Its design should make the user perceive Tulvex as innovative; I will incline for an out of the box design.
--Main bar
It will contain the site logo, a search bar, and four buttons, listed below.
---Notifications button
It will display a sidebar with containers; each container will have an icon, the notification, and one or two buttons; two example notifications and its respective buttons are in the second document.
It shall stand out when there are unseen notifications.
---Shopping cart button
A sidebar will be toggled on click with added product previews.
---Sell Button
---Account button
When clicked it will display a pane whose elements will depend on the user
status.
----If logged
It will display seller’s store image, a button linking to the main section of the account section, a button linking to in-process bought items of the account section, and a button linking to in-process sold items of the account section.
----If not logged
It will contain the elements for the user to either log in or register; for the former, email or username and password will be asked, for the latter, username, email, and password, this last one being asked twice.
--Product previews
Each, will have a title, a product image, and the product’s most important characteristics; most characteristics will have alongside an icon, which will display on mouse over the characteristic name, or, a name. Characteristics of two product categories whose product previews will contain an icon alongside are in the third document.
--Main page
Product previews of several categories will be displayed here; in order to reflect recommendation, some should have distinct size.
A list of categories will be present in this page; it may be toggled by a button contained in the main bar, or be displayed permanently.
A text conveying the message that all purchases made with Tulvex payment system are protected will be contained in a full width element which will be positioned below the main bar of this page; a “Learn more” link will be positioned in this element.
--Product page creation page
It will be displayed as part of the publication page.
It will be a "what you see is what you get" design system; the user will choose from several templates and fill the appropriate spaces; where text must be put, sample text will be present, and, where an image must, a plus sign and a “Add image” text will be present; submit please two templates; for the user to be able to add more content, at the bottom of the template there will be four layouts, upon click of one, it will be added.
Regarding the shipping menu, there will always be an empty box with a plus sign and a “Add shipping option” text, if clicked the user will be able to either fill it with company name, shipping time, and price, or to put the text “Arrange with seller” in it (if there is no other box with that text).
--Product page
It will not occupy the whole viewport; there will be vertical holes at the leftmost and rightmost parts of the viewport.
It will contain: price (which should include shipping in type one publications), sale price (for some product pages), countdown of sale price, average seller’s handling time, seller’s reputation indicator as measured by percentage of positive reviews received, seller’s store/profile image, seller’s username, a shipping menu consisting of boxes (selected will be displayed differently), “Buy” and “Add to cart” buttons, a section to view and ask questions, and seller provided images and text.
Previews of similar products will also be present.
Number of Pages Required
3 page

```html
<!DOCTYPE html>
<html lang="en">
<head>
<meta charset="utf-8">
<title>Tulvex — Store</title>
<link href="https://fonts.googleapis.com/css2?family=Open+Sans:wght@400;600;700&display=swap" rel="stylesheet">
<style>
:root{
  --blue:#2b86d8;
  --blue-dark:#1f6fbf;
  --orange:#f39c1f;
  --dark:#2e3338;
  --dark-line:#3d434a;
  --text:#444;
  --muted:#888;
  --line:#e3e6ea;
  --bg:#ffffff;
  --soft:#f4f6f8;
}
*{box-sizing:border-box;margin:0;padding:0}
html,body{width:1200px;height:2216px;overflow:hidden;background:var(--bg)}
body{font-family:"Open Sans",Arial,sans-serif;color:var(--text);font-size:13px;position:relative}
.abs{position:absolute}
a{color:inherit;text-decoration:none}

/* top strip */
.top-strip{top:0;left:0;width:1200px;height:36px;border-bottom:1px solid var(--line)}
.top-links{left:96px;top:11px;display:flex;gap:22px;font-size:11px;color:var(--muted)}
.top-links span::before{content:"";display:inline-block;width:8px;height:8px;background:#c6ccd3;border-radius:2px;margin-right:6px}
.top-account{right:96px;top:7px;display:flex;gap:12px;align-items:center;font-size:11px}
.top-account .pill{background:var(--blue);color:#fff;padding:4px 12px;border-radius:3px;font-weight:600}

/* header */
.brand{left:96px;top:48px;display:flex;align-items:center;gap:10px;font-size:40px;font-weight:700;color:var(--blue)}
.brand .mark{width:34px;height:34px;background:var(--orange);border-radius:4px}
.search{left:352px;top:86px;width:330px;height:32px;border:1px solid #cfd5db;border-radius:3px;font-size:11px;color:#aaa;padding:8px 10px}
.search-cat{left:684px;top:86px;width:92px;height:32px;background:var(--orange);color:#fff;font-size:11px;font-weight:600;text-align:center;line-height:32px;border-radius:3px}
.search-go{left:780px;top:86px;width:56px;height:32px;background:var(--blue);color:#fff;font-size:11px;font-weight:600;text-align:center;line-height:32px;border-radius:3px}
.notify{left:848px;top:86px;width:96px;height:32px;background:var(--orange);color:#fff;font-size:11px;font-weight:600;display:flex;align-items:center;justify-content:center;gap:6px;border-radius:3px}
.notify b{background:#fff;color:var(--orange);border-radius:8px;padding:0 5px;font-size:10px}
.cart{left:960px;top:86px;display:flex;align-items:center;gap:8px;font-size:11px}
.cart small{display:block;color:var(--muted);font-size:10px}

/* nav */
.nav{left:96px;top:160px;width:1008px;height:40px;border-bottom:3px solid var(--blue);display:flex}
.nav .cats{width:244px;background:var(--blue);color:#fff;font-weight:700;font-size:15px;padding:0 16px;display:flex;align-items:center;justify-content:space-between}
.nav ul{list-style:none;display:flex;margin-left:8px}
.nav li{width:98px;text-align:center;line-height:40px;font-size:11px;font-weight:600;color:#555}
.nav li.active{background:var(--blue);color:#fff}

/* sidebar */
.sidebar{left:96px;top:200px;width:244px;height:488px;background:var(--dark);color:#d9dde1}
.side-head{background:var(--blue);color:#fff;font-size:11px;font-weight:700;padding:8px 14px}
.side-list{list-style:none}
.side-list li{font-size:10.5px;padding:0 14px;height:29px;line-height:29px;border-bottom:1px solid var(--dark-line);display:flex;justify-content:space-between}
.side-list li::after{content:"›";color:#8a939c}

/* slider */
.slider{left:344px;top:200px;width:760px;height:488px;background:linear-gradient(120deg,#1f8f86 0%,#3bb3a6 35%,#cfd8c4 60%,#e9eee8 100%)}
.badge40{left:380px;top:400px;width:160px;height:90px;background:rgba(214,70,90,.8);color:#fff;font-size:44px;font-weight:300;text-align:center;line-height:90px}
.dots{right:112px;top:660px;display:flex;gap:6px}
.dots i{width:8px;height:8px;border-radius:50%;background:#fff;opacity:.6}
.dots i:first-child{opacity:1}

/* featured */
.section-title{left:96px;top:812px;font-size:17px;font-weight:700;color:#333}
.title-rule{left:96px;top:842px;width:836px;height:3px;background:var(--line)}
.title-rule::before{content:"";position:absolute;left:0;top:0;width:120px;height:3px;background:var(--blue)}
.product{top:860px;width:248px;height:404px;border:1px solid var(--line);text-align:center}
.product .bar{height:10px;background:var(--blue)}
.product .pic{margin:22px auto 0;width:160px;height:150px;border-radius:6px}
.product h3{font-size:13px;font-weight:700;margin-top:18px;color:#333}
.product .price{color:var(--orange);font-weight:700;font-size:12px;margin-top:6px}
.product p{font-size:10.5px;color:var(--muted);line-height:1.5;margin:8px 22px 0}
.product .stars{color:var(--orange);font-size:14px;margin-top:8px;letter-spacing:2px}
.product .stars span{color:#ccc}
.order{display:inline-block;background:var(--blue);color:#fff;font-size:10.5px;font-weight:700;padding:8px 18px;margin-top:14px;border-radius:2px}

.promo{left:948px;top:812px;width:156px;height:188px;background:linear-gradient(160deg,#3c4247,#1d2125)}
.promo-text{left:984px;top:860px;color:#fff}
.promo-text b{display:block;font-size:30px;line-height:1}
.promo-text span{font-size:13px}
.sellers{left:948px;top:1032px;width:156px;height:240px;border:1px solid var(--line)}
.sellers h4{background:var(--blue);color:#fff;font-size:11px;padding:9px 12px}
.sellers ul{list-style:none;padding:6px 10px}
.sellers li{font-size:9.5px;color:#666;padding:5px 0;border-bottom:1px dotted var(--line)}
.sellers li::before{content:"›";color:var(--blue);margin-right:6px}

.rule{left:96px;width:1008px;height:1px;background:var(--line)}

/* protection band */
.protect{left:96px;top:1370px;width:1008px;text-align:center}
.protect h2{font-size:37px;font-weight:400;color:var(--blue);line-height:1.35}
.protect p{font-size:11px;color:var(--muted);line-height:1.6;margin:26px 30px 0}
.learn{display:inline-block;margin-top:22px;background:var(--blue-dark);color:#fff;font-size:11px;font-weight:600;padding:10px 32px}

/* services */
.service{top:1712px;width:300px;display:flex;gap:14px}
.service .ico{flex:none;width:52px;height:52px;border-radius:50%;border:2px solid var(--blue);display:flex;align-items:center;justify-content:center}
.service h5{font-size:11px;font-weight:700;color:var(--blue);margin-top:4px}
.service p{font-size:10px;color:var(--muted);line-height:1.5;margin-top:4px}

/* newsletter */
.news{left:96px;top:1836px;width:1008px;height:56px;border-top:1px solid var(--line);border-bottom:1px solid var(--line);display:flex;align-items:center;padding:0 10px;gap:10px}
.news .label{font-size:11px;font-weight:700;color:var(--blue);flex:1}
.news .field{width:180px;height:26px;border:1px solid #cfd5db;font-size:10px;color:#aaa;padding:5px 8px}
.news .go{background:var(--blue);color:#fff;font-size:10px;font-weight:700;padding:6px 14px}
.social{display:flex;gap:6px;margin-left:20px}
.social i{width:22px;height:22px;border-radius:50%;background:var(--blue)}
.social i:nth-child(2){background:#4aa3df}
.social i:nth-child(3){background:#d9534f}
.social i:nth-child(4){background:#1d5fa3}

/* footer */
.fcol{top:1932px;width:230px}
.fcol h6{font-size:11px;font-weight:700;color:#333;margin-bottom:10px}
.fcol li{list-style:none;font-size:10px;color:var(--muted);line-height:1.75}
.cards{display:flex;gap:6px;margin-bottom:22px}
.cards i{width:36px;height:22px;border-radius:3px;background:#dfe4ea}
.cards i:nth-child(2){background:#c9d6e6}
.cards i:nth-child(3){background:#ecd9c9}
.copy{left:0;top:2176px;width:1200px;height:40px;border-top:3px solid var(--blue);font-size:10px;color:var(--muted);text-align:center;line-height:37px}
</style>
</head>
<body>

<div class="abs top-strip"></div>
<div class="abs top-links"><span>My account</span><span>Wishlist</span><span>Checkout</span><span>Register / Login</span></div>
<div class="abs top-account"><span class="pill">Notifications</span><span>Sell</span><span>Account ▾</span></div>

<div class="abs brand"><span class="mark"></span>Tulvex</div>
<div class="abs search">Search for products…</div>
<div class="abs search-cat">All ▾</div>
<div class="abs search-go">Search</div>
<div class="abs notify">Notifications <b>3</b></div>
<div class="abs cart">
  <svg width="26" height="24" viewBox="0 0 26 24"><path d="M1 3h4l3 13h13l3-9H7" fill="none" stroke="#2b86d8" stroke-width="2"/><circle cx="10" cy="20" r="2" fill="#2b86d8"/><circle cx="19" cy="20" r="2" fill="#2b86d8"/></svg>
  <div>Cart (2)<small>$ 598.00</small></div>
</div>

<div class="abs nav">
  <div class="cats">CATEGORIES <span>≡</span></div>
  <ul><li class="active">HOME</li><li>PRODUCTS</li><li>GALLERIES</li><li>ADVERTISE</li><li>VENDORS</li><li>CONTACT</li></ul>
</div>

<aside class="abs sidebar">
  <div class="side-head">WOMEN, CUSTOM BAGS</div>
  <ul class="side-list">
    <li>Fashion for Women</li><li>Evening Dresses</li><li>Casual Wear</li><li>Shoes &amp; Boots</li><li>Watches</li><li>Accessories</li><li>Jewellery</li>
  </ul>
  <div class="side-head">SHOES FOR MEN</div>
  <ul class="side-list">
    <li>Sneakers &amp; Trainers</li><li>Formal Shoes</li><li>Sports Wear</li><li>Outdoor Gear</li><li>Bags &amp; Wallets</li><li>Belts &amp; Ties</li><li>Home Appliances</li><li>Kitchen &amp; Dining</li>
  </ul>
</aside>

<div class="abs slider" role="img" aria-label="Banner photo: fashion model in sunglasses with a handbag, city backdrop"></div>
<div class="abs badge40">40%</div>
<div class="abs dots"><i></i><i></i><i></i></div>

<div class="abs section-title">FEATURE PRODUCTS</div>
<div class="abs title-rule"></div>

<div class="abs product" style="left:104px">
  <div class="bar"></div>
  <div class="pic" role="img" aria-label="Product photo: smartphones" style="background:linear-gradient(135deg,#2d2d33,#6b6f78)"></div>
  <h3>LAUDANTIUM, TOTAM</h3>
  <div class="price">$ 299.00</div>
  <p>Sed ut perspiciatis unde omnis iste natus error sit voluptatem.</p>
  <div class="stars">★★★★<span>★</span></div>
  <a class="order">ORDER NOW</a>
</div>
<div class="abs product" style="left:384px">
  <div class="bar"></div>
  <div class="pic" role="img" aria-label="Product photo: checked casual shirt" style="background:linear-gradient(135deg,#4a90c8,#9cc3e0)"></div>
  <h3>LAUDANTIUM, TOTAM</h3>
  <div class="price">$ 199.00</div>
  <p>Sed ut perspiciatis unde omnis iste natus error sit voluptatem.</p>
  <div class="stars">★★★★<span>★</span></div>
  <a class="order">ORDER NOW</a>
</div>
<div class="abs product" style="left:664px">
  <div class="bar"></div>
  <div class="pic" role="img" aria-label="Product photo: loudspeaker set" style="background:linear-gradient(135deg,#1c1c1f,#505258)"></div>
  <h3>LAUDANTIUM, TOTAM</h3>
  <div class="price">$ 289.00</div>
  <p>Sed ut perspiciatis unde omnis iste natus error sit voluptatem.</p>
  <div class="stars">★★★★<span>★</span></div>
  <a class="order">ORDER NOW</a>
</div>

<div class="abs promo" role="img" aria-label="Promotion photo: woman in fashion outfit"></div>
<div class="abs promo-text"><b>30%</b><span>Off<br>Big Sale</span></div>

<div class="abs sellers">
  <h4>TOP SELLERS</h4>
  <ul>
    <li>Lorem ipsum dolor sit amet elit</li><li>Sed ut perspiciatis unde omnis</li><li>Nemo enim ipsam voluptatem</li><li>Quis autem vel eum iure</li><li>At vero eos et accusamus</li><li>Nam libero tempore cum soluta</li><li>Temporibus autem quibusdam</li>
  </ul>
</div>

<div class="abs rule" style="top:1320px"></div>

<section class="abs protect">
  <h2>All purchases made with Tulvex Payment<br>System are Protected</h2>
  <p>Sed ut perspiciatis unde omnis iste natus error sit voluptatem accusantium doloremque laudantium, totam rem aperiam, eaque ipsa quae ab illo inventore veritatis et quasi architecto beatae vitae dicta sunt explicabo. Nemo enim ipsam voluptatem quia voluptas sit aspernatur aut odit aut fugit, sed quia consequuntur magni dolores eos qui ratione voluptatem sequi nesciunt neque porro quisquam.</p>
  <a class="learn">Learn more</a>
</section>

<div class="abs rule" style="top:1672px"></div>

<div class="abs service" style="left:124px">
  <div class="ico"><svg width="26" height="18" viewBox="0 0 26 18"><path d="M1 2h15v11H1zM16 6h5l4 4v3h-9z" fill="none" stroke="#2b86d8" stroke-width="2"/><circle cx="6" cy="15" r="2" fill="#2b86d8"/><circle cx="20" cy="15" r="2" fill="#2b86d8"/></svg></div>
  <div><h5>FREE SHIPPING</h5><p>Nemo enim ipsam voluptatem quia voluptas sit aspernatur aut odit.</p></div>
</div>
<div class="abs service" style="left:456px">
  <div class="ico"><svg width="24" height="24" viewBox="0 0 24 24"><path d="M20 12a8 8 0 1 1-3-6.3M17 2v4h-4" fill="none" stroke="#2b86d8" stroke-width="2"/></svg></div>
  <div><h5>RETURN EXCHANGE</h5><p>Nemo enim ipsam voluptatem quia voluptas sit aspernatur aut odit.</p></div>
</div>
<div class="abs service" style="left:788px">
  <div class="ico"><svg width="24" height="24" viewBox="0 0 24 24"><path d="M5 3l4 1 1 5-2 2a12 12 0 0 0 5 5l2-2 5 1 1 4-3 2C10 20 4 14 3 6z" fill="none" stroke="#2b86d8" stroke-width="2"/></svg></div>
  <div><h5>SUPPORT 24/7</h5><p>Nemo enim ipsam voluptatem quia voluptas sit aspernatur aut odit.</p></div>
</div>

<div class="abs news">
  <svg width="20" height="14" viewBox="0 0 20 14"><rect x="1" y="1" width="18" height="12" fill="none" stroke="#2b86d8" stroke-width="2"/><path d="M1 1l9 7 9-7" fill="none" stroke="#2b86d8" stroke-width="2"/></svg>
  <span class="label">GET OUR RECENT UPDATES ONLINE CHAT YOUR EMAIL ID</span>
  <span class="field">Your email address</span>
  <span class="go">SUBSCRIBE NOW</span>
  <span class="social"><i></i><i></i><i></i><i></i></span>
</div>

<div class="abs fcol" style="left:96px">
  <h6>PAYMENT OPTIONS</h6>
  <div class="cards"><i></i><i></i><i></i></div>
  <h6>OTHERS</h6>
  <ul><li>Blog</li><li>Affiliate Program</li><li>Contact</li></ul>
</div>
<div class="abs fcol" style="left:368px">
  <h6>SHIPPING INFORMATION</h6>
  <ul><li>Lorem ipsum dolor sit amet</li><li>Installation &amp; Exchange</li><li>Sed ut perspiciatis</li><li>Delivery times and rates</li><li>Nemo enim ipsam</li><li>Return &amp; Exchanges</li><li>Damaged items</li></ul>
</div>
<div class="abs fcol" style="left:624px">
  <h6>CUSTOMER CARE</h6>
  <ul><li>Contact us</li><li>Size chart</li><li>Payment</li><li>Shipping</li><li>International</li><li>Returns</li><li>FAQ</li><li>Privacy policy</li></ul>
</div>
<div class="abs fcol" style="left:880px">
  <h6>INFORMATION</h6>
  <ul><li>Terms &amp; Conditions</li><li>Product Recall</li><li>Discounts</li><li>Careers</li><li>Sitemap</li></ul>
</div>

<div class="abs copy">COPYRIGHT © 2015 TULVEX. ALL RIGHTS RESERVED</div>

</body>
</html>
```